Crisp by Zelvo Breeze, Can Label design

We are Zelvo Breeze, and we are based in Sydney Australia. We are a company that bottles and sells clean fresh quality Australain air. The air gets purified and filtered and then compressed into an aerosol can. We are after a label for our can with the product called "Crisp by Zelvo Breeze" We would like the design to look sophisticated and communicate purity. The can diameter is 65mm and the height is 168mm. So for a ducometn size this should be 201.6*172mm. There are rival products already on the market so we would like to stand out and look different from them. Looking forward to seeing your design.
Target Market(s)
Target market is Asia region. Both male and female from ages 18 and above.
Industry/Entity Type
Health And Wellness
Logo Text
Zelvo Breeze
Colors
Designer to choose colors to be used in the design.
Requirements
Must have
- The name "Crisp by Zelvo Breeze"
- On the back of the can it must have:
- Cans are filled with Australian air farmed in New South Wales, Australia
- contact us at www.crispzelvobreeze.example
- Directions of use: Remove cap from mask. Plug mask into valve. Place mask over mouth. Press valve and inhale.
- Caution: Do not place can in direct sunlight. Store can in temperatures under 50 Degrees Celsius. Contents of can are under high pressure, keep away from open flame and other heat sources.
- Ingredients: Air containing- Nitrogen, Oxygen, Argon and small amounts of other gasses.
Nice to have
- Something eye catching but not over the top
Should not have
- the phrase 100% pure Australian air. As this phrase is used by a competitor. A silver can with shades of blue as this is what a competitor uses.

```html
<!DOCTYPE html>
<html lang="en">
<head>
<meta charset="utf-8">
<title>Crisp by Zelvo Breeze – Can Label</title>
<link rel="stylesheet" href="https://fonts.googleapis.com/css2?family=Montserrat:wght@600;700&family=Didact+Gothic&display=swap">
<style>
  :root {
    --aqua-deep: #3fe0e6;
    --aqua-mid: #8cf0f2;
    --aqua-pale: #d8fafb;
    --white: #ffffff;
    --ink: #111111;
    --brand-blue: #1a3cf0;
    --logo-blue: #12b4ee;
    --mountain-dark: #6fd3dc;
    --mountain-light: #c9f3f5;
  }
  html, body {
    margin: 0;
    padding: 0;
    width: 1200px;
    height: 1025px;
    overflow: hidden;
    background: var(--white);
  }
  .label {
    position: relative;
    width: 1200px;
    height: 1025px;
    overflow: hidden;
    font-family: "Montserrat", sans-serif;
  }
  .panel {
    position: absolute;
    top: 12px;
    height: 1003px;
  }
  .panel--left {
    left: 14px;
    width: 397px;
    background: linear-gradient(180deg, var(--aqua-mid) 0%, var(--aqua-pale) 45%, var(--aqua-mid) 80%);
  }
  .panel--front {
    left: 411px;
    width: 381px;
    background: linear-gradient(90deg, var(--white) 0%, var(--white) 28%, var(--aqua-mid) 50%, var(--white) 72%, var(--white) 100%);
  }
  .panel--right {
    left: 792px;
    width: 396px;
    background: linear-gradient(180deg, var(--aqua-mid) 0%, var(--aqua-pale) 45%, var(--aqua-mid) 80%);
  }
  .glow {
    position: absolute;
    border-radius: 50%;
    background: radial-gradient(circle, rgba(255,255,255,0.95) 0%, rgba(255,255,255,0) 70%);
  }
  .mountains {
    position: absolute;
    left: 10px;
    top: 780px;
    width: 1180px;
    height: 235px;
    background: linear-gradient(180deg, rgba(201,243,245,0) 0%, var(--mountain-light) 22%, var(--mountain-dark) 60%, var(--mountain-light) 100%);
  }
  .block {
    position: absolute;
    text-align: center;
  }
  .heading {
    font-weight: 700;
    font-size: 18px;
    margin: 0 0 6px;
    letter-spacing: 0.3px;
  }
  .caution {
    left: 40px;
    top: 108px;
    width: 345px;
  }
  .caution .heading { color: var(--brand-blue); font-size: 16px; margin-bottom: 4px; }
  .caution p {
    margin: 0;
    color: var(--ink);
    font-weight: 700;
    font-size: 16px;
    line-height: 27px;
  }
  .directions {
    left: 46px;
    top: 654px;
    width: 320px;
    padding: 0 8px;
  }
  .directions .heading, .ingredients .heading { color: var(--ink); }
  .directions p, .ingredients p {
    margin: 0;
    color: var(--brand-blue);
    font-weight: 700;
    font-size: 18px;
  }
  .directions p { line-height: 30px; }
  .ingredients {
    left: 840px;
    top: 664px;
    width: 300px;
  }
  .ingredients p { line-height: 28px; }
  .origin {
    left: 860px;
    top: 142px;
    width: 272px;
    padding: 6px 0;
    background: rgba(255,255,255,0.35);
    border-radius: 6px;
    font-family: "Didact Gothic", sans-serif;
    font-size: 19px;
    line-height: 36px;
  }
  .origin .blue { color: var(--brand-blue); }
  .origin .dark { color: var(--ink); }
  .contact {
    left: 820px;
    top: 892px;
    width: 320px;
    font-weight: 700;
  }
  .contact .lead { margin: 0; color: var(--ink); font-size: 21px; line-height: 30px; }
  .contact .url { margin: 0; color: var(--brand-blue); font-size: 19px; line-height: 28px; }
  .brand {
    position: absolute;
    display: flex;
    align-items: center;
    gap: 10px;
    transform: translate(-50%, -50%);
    font-family: "Montserrat", sans-serif;
    font-weight: 700;
    color: var(--logo-blue);
    white-space: nowrap;
  }
  .brand__dot {
    flex: none;
    border-radius: 50%;
    background: var(--logo-blue);
  }
  .brand__name { line-height: 1.05; text-align: left; }
  .brand--side { font-size: 30px; }
  .brand--side .brand__dot { width: 30px; height: 30px; }
  .brand--front { font-size: 36px; }
  .brand--front .brand__dot { width: 38px; height: 38px; }
  .brand--left { left: 213px; top: 458px; }
  .brand--front { left: 602px; top: 497px; }
  .brand--right { left: 990px; top: 458px; }
</style>
</head>
<body>
<main class="label">
  <section class="panel panel--left">
    <span class="glow" style="left:70px;top:340px;width:260px;height:280px;"></span>
  </section>
  <section class="panel panel--front">
    <span class="glow" style="left:60px;top:380px;width:260px;height:300px;"></span>
  </section>
  <section class="panel panel--right">
    <span class="glow" style="left:70px;top:340px;width:260px;height:280px;"></span>
  </section>

  <div class="mountains" role="img" aria-label="Snowy mountain range photograph in pale aqua tones"></div>

  <div class="block caution">
    <h2 class="heading">CAUTION:</h2>
    <p>Do not place can in direct sunlight. Store can in temperatures under 50 Degrees Celsius. Contents of can are under high pressure, keep away from open flame and other heat sources.</p>
  </div>

  <div class="brand brand--side brand--left">
    <span class="brand__name">Crisp by<br>Zelvo Breeze</span>
    <span class="brand__dot"></span>
  </div>

  <div class="block directions">
    <h2 class="heading">DIRECTIONS OF USE:</h2>
    <p>Remove cap from mask. Plug mask into valve. Place mask over mouth. Press valve and inhale.</p>
  </div>

  <div class="brand brand--front">
    <span class="brand__name">Crisp by<br>Zelvo Breeze</span>
    <span class="brand__dot"></span>
  </div>

  <div class="block origin">
    <span class="blue">Cans are filled with Australian<br>air farmed in</span><br>
    <span class="dark">New South Wales, Australia.</span>
  </div>

  <div class="brand brand--side brand--right">
    <span class="brand__name">Crisp by<br>Zelvo Breeze</span>
    <span class="brand__dot"></span>
  </div>

  <div class="block ingredients">
    <h2 class="heading">INGREDIENTS:</h2>
    <p>Air containing- Nitrogen, Oxygen, Argon and small amounts of other gasses.</p>
  </div>

  <div class="block contact">
    <p class="lead">Contact us at</p>
    <p class="url">www.crispzelvobreeze.example</p>
  </div>
</main>
</body>
</html>
```